Steady Harbour Coaching Business Card

We need a business card for a new business based in Sydney Australia called "Steady Harbour Coaching". The business provides the following:
1. Resilience systems for individuals - Developing personalised resilience programs that increase stress tolerance, improve work effectiveness and minimise stress responses to challenge.
2. Group Resilience Training for Leaders and managers - Delivering Resilience training packages and ongoing support to leadership cadres within organisations.
3. High Risk Resilience Training - providing resilience training for High Risk professions such as emergency responders, military and police.

Target Market(s)

Corporate / Military / Emergency Responders

Industry/Entity Type

Leadership

Contact Information for Business Card

Steady Harbour Coaching, Rowan Petrakis, 7/18 Wexley St Dunmore 2093, quiet.tide.notes@mailvane.net, www.steadyharbourcoaching.net.au, M# 0471635082
Personalised Mental Resilience Systems for leaders and high risk professions

Requirements
Must have
• 1. Creation of a logo/graphic - to include 3 elements:
a. Military
b.Corporate
c. Emergency Responder.

As long as those 3 elements are included - I am open to any potential designs. Preference given to those who can create a logo out of the above three elements.

```html
<!DOCTYPE html>
<html lang="en">
<head>
<meta charset="utf-8">
<title>Steady Harbour Coaching – Business Card</title>
<link href="https://fonts.googleapis.com/css2?family=PT+Sans:wght@400;700&display=swap" rel="stylesheet">
<style>
  :root {
    --page-bg: #e4e4e2;
    --card-white: #ffffff;
    --card-fade: #e9e9e9;
    --band-dark: #161616;
    --band-mid: #4a4a4a;
    --title-grey: #4d4d4d;
    --contact-white: #f4f4f4;
    --figure-tone: #2a2a2a;
  }
  html, body {
    margin: 0;
    padding: 0;
    width: 1200px;
    height: 992px;
    overflow: hidden;
    background: var(--page-bg);
  }
  .business-card {
    position: absolute;
    left: 100px;
    top: 210px;
    width: 1000px;
    height: 572px;
    border-radius: 6px;
    overflow: hidden;
    background: linear-gradient(160deg, var(--card-white) 0%, var(--card-white) 55%, var(--card-fade) 100%);
    box-shadow: 0 18px 40px rgba(0,0,0,0.22);
    font-family: "PT Sans", sans-serif;
  }
  .dark-band {
    position: absolute;
    inset: 0;
    width: 1000px;
    height: 572px;
  }
  .team-figures {
    position: absolute;
    left: 50px;
    top: 100px;
    width: 220px;
    height: 215px;
    background: radial-gradient(ellipse at center, #3a3a3a 0%, var(--figure-tone) 55%, rgba(42,42,42,0.0) 72%);
  }
  .business-name {
    position: absolute;
    left: 290px;
    top: 68px;
    margin: 0;
    font-size: 40px;
    font-weight: 400;
    color: var(--title-grey);
    letter-spacing: 0.2px;
  }
  .contact-list {
    position: absolute;
    left: 470px;
    top: 262px;
    margin: 0;
    padding: 0;
    list-style: none;
    color: var(--contact-white);
    font-size: 27px;
  }
  .contact-list li {
    display: flex;
    align-items: center;
    height: 50px;
  }
  .contact-list svg {
    width: 18px;
    height: 18px;
    margin-right: 12px;
    fill: var(--contact-white);
    flex: none;
  }
  .contact-list .web-line {
    margin-top: 8px;
    font-size: 25px;
  }
  .person-name {
    position: absolute;
    left: 62px;
    top: 500px;
    margin: 0;
    font-size: 30px;
    font-weight: 400;
    color: var(--contact-white);
  }
</style>
</head>
<body>
  <div class="business-card">
    <svg class="dark-band" viewBox="0 0 1000 572" aria-hidden="true">
      <defs>
        <linearGradient id="bandShade" x1="0" y1="1" x2="1" y2="0">
          <stop offset="0" stop-color="#1b1b1b"/>
          <stop offset="0.45" stop-color="#2e2e2e"/>
          <stop offset="0.75" stop-color="#4a4a4a"/>
          <stop offset="1" stop-color="#222"/>
        </linearGradient>
      </defs>
      <path d="M0,470 C200,380 380,220 1000,60 L1000,572 L0,572 Z" fill="url(#bandShade)"/>
    </svg>

    <div class="team-figures" role="img" aria-label="Silhouettes of a soldier, a corporate professional and an emergency responder standing in a row"></div>

    <h1 class="business-name">Steady Harbour Coaching</h1>

    <ul class="contact-list">
      <li>
        <svg viewBox="0 0 20 20" aria-hidden="true"><path d="M10 1a6 6 0 0 0-6 6c0 4.5 6 12 6 12s6-7.5 6-12a6 6 0 0 0-6-6zm0 8.5a2.5 2.5 0 1 1 0-5 2.5 2.5 0 0 1 0 5z"/></svg>
        7/18 Wexley St Dunmore 2093 ,
      </li>
      <li>
        <svg viewBox="0 0 20 20" aria-hidden="true"><path d="M5 2l3 4-2 2c1 2.5 3 4.5 5.5 5.5l2-2 4 3-2 3C9 17 3 11 2 5z"/></svg>
        0471635082
      </li>
      <li>
        <svg viewBox="0 0 20 20" aria-hidden="true"><path d="M2 4h16v12H2z M2 4l8 7 8-7" stroke="#161616" stroke-width="1.4"/></svg>
        quiet.tide.notes@mailvane.net
      </li>
      <li class="web-line">
        <svg viewBox="0 0 20 20" aria-hidden="true"><circle cx="10" cy="10" r="8"/></svg>
        www.steadyharbourcoaching.net.au
      </li>
    </ul>

    <p class="person-name">Rowan Petrakis</p>
  </div>
</body>
</html>
```